Creating a Label for the Wine "Sing by Candle"

As the name suggest, this wine is the one people must to take home. Sing by candle is the perfect wine to drink at home with you family and friends. Customers should be able to associate this label with happy moments spent with their loved ones. The dimensions can be between 9cm x 11,5 and 12cm x 8 cm.

```html
<!DOCTYPE html>
<html lang="en">
<head>
<meta charset="utf-8">
<title>Sing by Candle – Malbec 2014 Label</title>
<link rel="stylesheet" href="https://fonts.googleapis.com/css2?family=Cabin:wght@700&family=Cormorant+Garamond:wght@500;600&display=swap">
<style>
  :root {
    --backdrop: #1e1e1f;
    --label-paper: #f7f7f5;
    --ink-dark: #2b2b2e;
    --leaf-green: #8aa61c;
  }
  * { margin: 0; padding: 0; box-sizing: border-box; }
  html, body {
    width: 1200px;
    height: 3025px;
    overflow: hidden;
    background: var(--backdrop);
  }
  .canvas {
    position: relative;
    width: 1200px;
    height: 3025px;
    background: var(--backdrop);
  }
  .wine-label {
    position: absolute;
    left: 100px;
    top: 875px;
    width: 1000px;
    height: 1275px;
    background: var(--label-paper);
  }
  .brand {
    position: absolute;
    left: 120px;
    top: 430px;
    display: flex;
    align-items: flex-start;
    gap: 22px;
  }
  .brand-dot {
    width: 34px;
    height: 34px;
    margin-top: 40px;
    border-radius: 50%;
    background: var(--leaf-green);
  }
  .brand-name {
    display: flex;
    flex-direction: column;
    align-items: flex-end;
    font-family: "Cabin", sans-serif;
    font-weight: 700;
    color: var(--ink-dark);
    line-height: 0.86;
    letter-spacing: -4px;
  }
  .brand-name-top { font-size: 140px; }
  .brand-name-main { font-size: 205px; }
  .varietal {
    position: absolute;
    left: 0;
    width: 100%;
    top: 1060px;
    text-align: center;
    font-family: "Cormorant Garamond", serif;
    font-weight: 600;
    font-size: 42px;
    letter-spacing: 6px;
    color: var(--ink-dark);
  }
  .vintage {
    position: absolute;
    left: 0;
    width: 100%;
    top: 1112px;
    text-align: center;
    font-family: "Cormorant Garamond", serif;
    font-weight: 600;
    font-size: 42px;
    letter-spacing: 9px;
    color: var(--leaf-green);
  }
</style>
</head>
<body>
  <main class="canvas">
    <section class="wine-label">
      <div class="brand">
        <span class="brand-dot"></span>
        <h1 class="brand-name">
          <span class="brand-name-top">Sing by</span>
          <span class="brand-name-main">candle</span>
        </h1>
      </div>
      <p class="varietal">MALBEC</p>
      <p class="vintage">2014</p>
    </section>
  </main>
</body>
</html>
```